Employee Benefits and Insurance Consulting

We are an existing company with over 30 years experience but are changing our name. We would like a simple design with grey tones.

Industry/Entity Type

Insurance

Contact Information for Business Card

Marlow Benefits Consulting
Gerald P Odell CEO
5172 Brackenfield Road
Louisville, TN 37777
gerald@marlowbx.com
865-412-3396 - O
865-247-5081 - C

```html
<!DOCTYPE html>
<html lang="en">
<head>
<meta charset="utf-8">
<title>Marlow Benefits Consulting – Business Card</title>
<link rel="stylesheet" href="https://fonts.googleapis.com/css2?family=Jost:wght@400&display=swap">
<style>
  :root {
    --stage: #d8d5d1;
    --card-dark: #141414;
    --card-light: #ffffff;
    --ink-light: #e6e6e6;
    --ink-grey: #8a8a8a;
    --ink-mid: #777777;
    --shadow: rgba(0, 0, 0, 0.28);
  }
  * { box-sizing: border-box; margin: 0; padding: 0; }
  html, body {
    width: 1200px;
    height: 900px;
    overflow: hidden;
    background: var(--stage);
    font-family: "Jost", "Futura", sans-serif;
    font-weight: 400;
  }
  .stage { position: relative; width: 1200px; height: 900px; }
  .card {
    position: absolute;
    width: 600px;
    height: 343px;
    border-radius: 22px;
    box-shadow: 0 14px 30px var(--shadow);
  }
  .card--front { left: 110px; top: 80px; background: var(--card-dark); }
  .card--back  { left: 490px; top: 470px; background: var(--card-light); }

  .brand {
    position: absolute;
    text-transform: uppercase;
    font-weight: 400;
    line-height: 1;
  }
  .brand__name { display: block; letter-spacing: 0.42em; }
  .brand__tagline { display: block; letter-spacing: 0.06em; margin-top: 8px; }

  .card--front .brand {
    left: 0; right: 0; top: 128px;
    text-align: center;
    color: var(--ink-light);
  }
  .card--front .brand__name { font-size: 52px; padding-left: 0.42em; }
  .card--front .brand__tagline { font-size: 19px; }

  .card--back .brand {
    left: 40px; top: 150px;
    color: var(--ink-grey);
  }
  .card--back .brand__name { font-size: 40px; }
  .card--back .brand__tagline { font-size: 15px; }

  .contact {
    position: absolute;
    left: 330px; top: 62px;
    color: var(--ink-mid);
    text-transform: uppercase;
  }
  .contact__name { font-size: 21px; letter-spacing: 0.04em; line-height: 1.1; }
  .contact__role { font-size: 17px; letter-spacing: 0.3em; margin: 0 0 14px 14px; }
  .contact__list { list-style: none; font-size: 15px; letter-spacing: 0.03em; }
  .contact__item {
    display: flex;
    align-items: flex-start;
    gap: 10px;
    margin: 0 0 7px 24px;
    line-height: 1.35;
  }
  .contact__item svg { flex: none; width: 14px; height: 14px; margin-top: 3px; fill: var(--ink-mid); }
  .contact__email { text-transform: uppercase; }
</style>
</head>
<body>
<main class="stage">
  <section class="card card--front" aria-label="Card front">
    <div class="brand">
      <span class="brand__name">Marlow</span>
      <span class="brand__tagline">Benefits Consulting</span>
    </div>
  </section>

  <section class="card card--back" aria-label="Card back">
    <div class="brand">
      <span class="brand__name">Marlow</span>
      <span class="brand__tagline">Benefits Consulting</span>
    </div>

    <div class="contact">
      <p class="contact__name">Gerald P Odell</p>
      <p class="contact__role">CEO</p>
      <ul class="contact__list">
        <li class="contact__item">
          <svg viewBox="0 0 14 14" aria-hidden="true"><path d="M7 0a5 5 0 0 0-5 5c0 3.6 5 9 5 9s5-5.4 5-9a5 5 0 0 0-5-5zm0 7a2 2 0 1 1 0-4 2 2 0 0 1 0 4z"/></svg>
          <span>5172 Brackenfield Road<br>Louisville, TN 37777</span>
        </li>
        <li class="contact__item">
          <svg viewBox="0 0 14 14" aria-hidden="true"><path d="M0 3h14v9H0zM1 4l6 4.5L13 4v-.2H1z" fill-rule="evenodd"/></svg>
          <span class="contact__email">gerald@marlowbx.com</span>
        </li>
        <li class="contact__item">
          <svg viewBox="0 0 14 14" aria-hidden="true"><path d="M1 4c0-2 12-2 12 0v1.5H10V4.2H4v1.3H1zM2 7h10l1 6H1zm5 1.5a2 2 0 1 0 0 4 2 2 0 0 0 0-4z"/></svg>
          <span>865-412-3396</span>
        </li>
        <li class="contact__item">
          <svg viewBox="0 0 14 14" aria-hidden="true"><path d="M4 0h6a1 1 0 0 1 1 1v12a1 1 0 0 1-1 1H4a1 1 0 0 1-1-1V1a1 1 0 0 1 1-1zm.5 1.5v9.5h5V1.5zM7 11.7a.7.7 0 1 0 0 1.4.7.7 0 0 0 0-1.4z" fill-rule="evenodd"/></svg>
          <span>865-247-5081</span>
        </li>
      </ul>
    </div>
  </section>
</main>
</body>
</html>
```